2 Page Brochure - Commercial Roofing Company

We are looking for a double sided brochure, full color, for our commercial roofing company that tells customers a little bit about the company, what we do, and shows a few pictures.
The brochure would need to have our logo and color scheme that coordinates with that logo.
I have uploaded our logo, some ideas I had, and then the idea list also has our website on there if you'd like to take a look around there for some more ideas.
I have also uploaded some photos we'd like to use.
Page size should be 8.5" x 11".
Target Market(s)
Commercial Property Owners
Other font styles liked:
- Match logo font ideally so it's cohesive, but whatever looks best

```html
<!DOCTYPE html>
<html lang="en">
<head>
<meta charset="utf-8">
<title>Summit Ridge Roofing – Brochure</title>
<link href="https://fonts.googleapis.com/css2?family=Montserrat:wght@400;500;600;700;800&display=swap" rel="stylesheet">
<style>
:root{
  --stage:#c9c9c9;
  --ink:#2a2b30;
  --ink-deep:#212226;
  --orange:#ee5a24;
  --orange-soft:#f26a2e;
  --white:#ffffff;
  --paper:#ececec;
  --gold:#c9a24a;
  --muted:#d7d7d7;
}
*{box-sizing:border-box;margin:0;padding:0}
html,body{width:1200px;height:3243px;overflow:hidden}
body{background:var(--stage);font-family:'Montserrat',sans-serif;color:var(--ink);position:relative}
.page{position:absolute;left:50px;width:1100px;height:848px;overflow:hidden;box-shadow:0 6px 18px rgba(0,0,0,.25)}
.page--cover{top:740px;background:var(--paper)}
.page--inside{top:1648px;background:var(--ink)}
.art{position:absolute;left:0;top:0;width:1100px;height:848px}
.abs{position:absolute}

/* cover */
.contact{left:150px;top:50px;width:240px;text-align:center}
.contact-icons{display:flex;justify-content:center;gap:6px;margin-bottom:6px}
.contact-icons svg{width:26px;height:26px}
.contact-phone{font-weight:700;font-size:32px;color:var(--orange);letter-spacing:.5px;line-height:1.2}
.contact-line{font-weight:500;font-size:17px;color:var(--ink-deep);line-height:1.35}
.contact-web{margin:4px 0 6px}
.contact-rule{width:52px;height:3px;background:var(--orange);margin:12px auto 0}
.brand-top{left:690px;top:36px;width:266px;text-align:center;font-weight:800;font-size:34px;line-height:1.02;color:var(--ink-deep);letter-spacing:.5px}
.band{left:0;top:658px;width:1100px;height:190px;background:var(--ink)}
.band-brand{left:50px;top:40px;width:230px;text-align:center;font-weight:800;font-size:26px;line-height:1.05;color:var(--white)}
.band-divider{left:296px;top:26px;width:3px;height:80px;background:var(--orange)}
.band-badge{left:331px;top:32px;width:90px;height:68px;border:3px solid var(--gold);background:transparent}
.band-roc{left:129px;top:129px;width:282px;height:27px;border:2px solid var(--orange);color:var(--orange);font-weight:700;font-size:16px;text-align:center;line-height:23px}
.tagline{left:600px;top:22px;width:445px;text-align:center;font-weight:800;font-size:40px;line-height:1.12;color:var(--white)}
.tagline .accent{color:var(--orange)}
.tagline-web{left:621px;top:131px;width:402px;height:25px;background:var(--orange);color:var(--white);font-weight:600;font-size:15px;letter-spacing:4px;text-align:center;line-height:25px}

/* inside */
.about{left:100px;top:130px;width:416px;text-align:right;color:var(--white)}
.heading{font-weight:800;font-size:27px;letter-spacing:.3px;line-height:1.1}
.heading .accent,.accent{color:var(--orange)}
.heading-rule{width:46px;height:3px;background:var(--orange);margin:6px 0 16px auto}
.about p{font-size:11.2px;line-height:1.42;font-weight:500;margin-bottom:12px}
.services{left:40px;top:536px;width:452px;color:var(--white)}
.services .heading{text-align:center;font-size:25px}
.services .heading-rule{margin:5px auto 0 auto;width:40px}
.service-grid{display:grid;grid-template-columns:repeat(3,1fr);row-gap:36px;margin-top:26px}
.service{text-align:center;font-size:11.5px;font-weight:700;line-height:1.3}
.service svg{width:46px;height:46px;display:block;margin:0 auto 6px}
.service .accent{display:block}
.products{left:579px;top:136px;width:490px;color:var(--white)}
.products .heading{font-size:26px;line-height:1.12}
.product-list{margin-top:30px;font-size:11.8px;font-weight:500;line-height:2.4}
.product-list .sep{display:inline-block;width:1.5px;height:14px;background:var(--white);vertical-align:middle;margin:0 6px}
.certified{left:579px;top:396px;width:484px;text-align:center;color:var(--white)}
.certified .heading{font-size:25px;line-height:1.22}
.badge-grid{left:579px;top:489px;width:484px;display:grid;grid-template-columns:repeat(3,152px);grid-auto-rows:110px;column-gap:14px;row-gap:10px}
.badge-cell{background:var(--white);display:flex;align-items:center;justify-content:center}
.more{left:579px;top:736px;width:484px;text-align:center;font-size:12px;font-weight:600;letter-spacing:4px;color:var(--white)}
.more .accent{color:var(--orange)}
.serving{left:579px;top:775px;width:484px;height:36px;display:flex;font-weight:700;font-size:14px}
.serving-label{width:108px;border:2px solid var(--orange);color:var(--orange);text-align:center;line-height:32px}
.serving-text{flex:1;background:var(--orange);color:var(--white);text-align:center;line-height:36px}
</style>
</head>
<body>

<!-- Cover spread -->
<section class="page page--cover">
  <svg class="art" viewBox="0 0 1100 848" aria-hidden="false">
    <defs>
      <linearGradient id="roofTexture" x1="0" y1="0" x2="1" y2="1">
        <stop offset="0" stop-color="#f4f4f4"/><stop offset="1" stop-color="#dadada"/>
      </linearGradient>
      <linearGradient id="landscape" x1="0" y1="0" x2="0" y2="1">
        <stop offset="0" stop-color="#b7c4d3"/><stop offset=".45" stop-color="#9aa1b3"/>
        <stop offset=".6" stop-color="#8a8ea0"/><stop offset=".78" stop-color="#cdc9c1"/>
        <stop offset="1" stop-color="#4f8a3a"/>
      </linearGradient>
      <linearGradient id="shotA" x1="0" y1="0" x2="0" y2="1"><stop offset="0" stop-color="#a8b8c8"/><stop offset="1" stop-color="#6e6a66"/></linearGradient>
      <linearGradient id="shotB" x1="0" y1="0" x2="0" y2="1"><stop offset="0" stop-color="#5f88b8"/><stop offset="1" stop-color="#3d7a6e"/></linearGradient>
      <linearGradient id="shotC" x1="0" y1="0" x2="0" y2="1"><stop offset="0" stop-color="#7fa6cf"/><stop offset="1" stop-color="#d8d2c6"/></linearGradient>
    </defs>
    <rect width="1100" height="658" fill="url(#roofTexture)" role="img" aria-label="Soft white roof membrane texture"/>
    <polygon points="818,166 1100,319 1100,658 0,658 0,620 520,330" fill="url(#landscape)" role="img" aria-label="Aerial view of commercial rooftops with mountains on the horizon"/>
    <polyline points="520,330 818,166 1100,319" fill="none" stroke="#2a2b30" stroke-width="2"/>
    <polygon points="35,360 200,288 200,490 35,578" fill="url(#shotA)" role="img" aria-label="Building parapet and roof edge"/>
    <polygon points="200,288 360,219 360,405 200,490" fill="url(#shotB)" role="img" aria-label="Metal roof panels on a storefront"/>
    <polygon points="360,219 519,150 519,320 360,405" fill="url(#shotC)" role="img" aria-label="Coated flat roof with vents"/>
    <polygon points="35,360 519,150 519,320 35,578" fill="none" stroke="#ee5a24" stroke-width="7"/>
    <line x1="200" y1="288" x2="200" y2="490" stroke="#ee5a24" stroke-width="5"/>
    <line x1="360" y1="219" x2="360" y2="405" stroke="#ee5a24" stroke-width="5"/>
  </svg>

  <div class="abs contact">
    <div class="contact-icons">
      <svg viewBox="0 0 26 26"><circle cx="13" cy="13" r="11" fill="none" stroke="#2a2b30" stroke-width="1.6"/><path d="M9 8c0 5 4 9 9 9l1-2-3-1-1 1c-2-1-3-2-4-4l1-1-1-3z" fill="#ee5a24"/></svg>
      <svg viewBox="0 0 26 26"><circle cx="13" cy="13" r="11" fill="none" stroke="#2a2b30" stroke-width="1.6"/><circle cx="13" cy="13" r="6" fill="none" stroke="#ee5a24" stroke-width="1.5"/><path d="M7 13h12M13 7c-3 4-3 8 0 12M13 7c3 4 3 8 0 12" fill="none" stroke="#ee5a24" stroke-width="1.2"/></svg>
      <svg viewBox="0 0 26 26"><circle cx="13" cy="13" r="11" fill="none" stroke="#2a2b30" stroke-width="1.6"/><path d="M13 19s-5-5-5-8a5 5 0 0 1 10 0c0 3-5 8-5 8z" fill="#ee5a24"/><circle cx="13" cy="11" r="1.8" fill="#fff"/></svg>
    </div>
    <div class="contact-phone">602-555-0148</div>
    <div class="contact-line contact-web">www.summitridge-roofing.com</div>
    <div class="contact-line">214 W Canyon Rd.</div>
    <div class="contact-line">Prescott AZ 86301</div>
    <div class="contact-rule"></div>
  </div>

  <div class="abs brand-top">SUMMIT RIDGE<br>ROOFING</div>

  <div class="abs band">
    <div class="abs band-brand">SUMMIT RIDGE<br>ROOFING</div>
    <div class="abs band-divider"></div>
    <div class="abs band-badge" role="img" aria-label="Certified contractor badge"></div>
    <div class="abs band-roc">AZ ROC 512730</div>
    <div class="abs tagline"><span class="accent">QUALITY</span> ROOFING<br>YOU CAN TRUST</div>
    <div class="abs tagline-web">www.summitridge-roofing.com</div>
  </div>
</section>

<!-- Inside spread -->
<section class="page page--inside">
  <svg class="art" viewBox="0 0 1100 848">
    <defs>
      <linearGradient id="storefront" x1="0" y1="0" x2="0" y2="1"><stop offset="0" stop-color="#8fb0d6"/><stop offset=".55" stop-color="#c9d6e4"/><stop offset="1" stop-color="#8a7f74"/></linearGradient>
      <linearGradient id="flatroof" x1="0" y1="0" x2="0" y2="1"><stop offset="0" stop-color="#8fb2d9"/><stop offset=".4" stop-color="#c7b59a"/><stop offset="1" stop-color="#6f737a"/></linearGradient>
    </defs>
    <polygon points="0,0 565,0 0,306" fill="url(#storefront)" role="img" aria-label="Single-storey commercial building with a new roof"/>
    <polygon points="565,0 1100,0 1100,234" fill="url(#flatroof)" role="img" aria-label="Large flat commercial roof with rooftop units"/>
  </svg>

  <div class="abs about">
    <h2 class="heading accent">ABOUT US</h2>
    <div class="heading-rule"></div>
    <p>Summit Ridge Roofing opened the doors in 1984,<br>and we've since installed, serviced, maintained, and<br>coated thousands of commercial roofs around the state<br>of Arizona, in the many climate regions of the state.</p>
    <p>Though we all live here for the constant sunshine, Arizona is one of the<br>harshest environments in the US for roofs. Constant sun, heat, dryness,<br>and then the torrential monsoon downpours all test the limits of your roof.</p>
    <p>We work with you to come up with a solution that works for your roof and<br>will keep your business dry for years to come. Then, our team of project<br>managers, superintendents, foremen, and field workers all come togeth-<br>er to execute on that plan and install a quality roof.</p>
    <p>We are certified with many different manufacturers, so we're able to offer<br>custom solutions to solve your issues, that will also often come with repu-<br>table manufacturer warranties.</p>
  </div>

  <div class="abs services">
    <h2 class="heading"><span class="accent">SERVICES</span> WE OFFER</h2>
    <div class="heading-rule"></div>
    <div class="service-grid">
      <div class="service">
        <svg viewBox="0 0 46 46"><circle cx="23" cy="23" r="20" fill="none" stroke="#ee5a24" stroke-width="2"/><path d="M15 31l16-16M15 15l16 16" stroke="#ee5a24" stroke-width="2.4" stroke-linecap="round"/></svg>
        <span class="accent">NEW ROOF</span>INSTALLATION
      </div>
      <div class="service">
        <svg viewBox="0 0 46 46"><circle cx="23" cy="23" r="20" fill="none" stroke="#ee5a24" stroke-width="2"/><path d="M13 25l10-9 10 9v8H13z" fill="none" stroke="#ee5a24" stroke-width="2"/><path d="M18 29h10" stroke="#ee5a24" stroke-width="2"/></svg>
        <span class="accent">RE-ROOFING</span>
      </div>
      <div class="service">
        <svg viewBox="0 0 46 46"><circle cx="23" cy="23" r="20" fill="none" stroke="#ee5a24" stroke-width="2"/><circle cx="23" cy="23" r="7" fill="none" stroke="#ee5a24" stroke-width="2"/><path d="M23 12v4M23 30v4M12 23h4M30 23h4" stroke="#ee5a24" stroke-width="2"/></svg>
        <span class="accent">ROOF MAINTENANCE</span>AND SERVICE
      </div>
      <div class="service">
        <svg viewBox="0 0 46 46"><circle cx="23" cy="23" r="20" fill="none" stroke="#ee5a24" stroke-width="2"/><circle cx="21" cy="21" r="7" fill="none" stroke="#ee5a24" stroke-width="2"/><path d="M26 26l7 7" stroke="#ee5a24" stroke-width="2.4" stroke-linecap="round"/></svg>
        <span class="accent">ROOF</span>INSPECTIONS
      </div>
      <div class="service">
        <svg viewBox="0 0 46 46"><circle cx="23" cy="23" r="20" fill="none" stroke="#ee5a24" stroke-width="2"/><rect x="14" y="13" width="16" height="8" rx="2" fill="none" stroke="#ee5a24" stroke-width="2"/><path d="M30 17h3v7h-10v9" fill="none" stroke="#ee5a24" stroke-width="2"/></svg>
        <span class="accent">ROOF</span>COATINGS
      </div>
      <div class="service">
        <svg viewBox="0 0 46 46"><circle cx="23" cy="23" r="20" fill="none" stroke="#ee5a24" stroke-width="2"/><rect x="13" y="13" width="8" height="8" fill="none" stroke="#ee5a24" stroke-width="2"/><rect x="25" y="13" width="8" height="8" fill="none" stroke="#ee5a24" stroke-width="2"/><rect x="13" y="25" width="8" height="8" fill="none" stroke="#ee5a24" stroke-width="2"/><path d="M29 25v8M25 29h8" stroke="#ee5a24" stroke-width="2"/></svg>
        <span class="accent">AND MANY</span>MORE...
      </div>
    </div>
  </div>

  <div class="abs products">
    <h2 class="heading"><span class="accent">WE INSTALLS</span><br>THE FOLLOWING<br>PRODUCTS</h2>
    <div class="product-list">
      TPO<span class="sep"></span>PVC<span class="sep"></span>MODIFIED BITUMEN<span class="sep"></span>SILICONE COATINGS<br>
      ACRYLIC COATINGS<span class="sep"></span>SHINGLE<span class="sep"></span>METAL&nbsp;&nbsp; TILE<br>
      SPRAY POLYURETHANE FOAM<span class="sep"></span>AND MORE...
    </div>
  </div>

  <div class="abs certified">
    <h2 class="heading"><span class="accent">CERTIFIED WITH THE</span><br>FOLLOWING MANUFACTURERS</h2>
  </div>

  <div class="abs badge-grid">
    <div class="badge-cell" role="img" aria-label="Manufacturer certification"><svg width="84" height="60"><rect x="2" y="2" width="80" height="56" fill="none" stroke="#c9a24a" stroke-width="3"/></svg></div>
    <div class="badge-cell" role="img" aria-label="Manufacturer certification"><svg width="90" height="24"><rect x="0" y="4" width="90" height="16" fill="#4a4b50"/></svg></div>
    <div class="badge-cell" role="img" aria-label="Manufacturer certification"><svg width="70" height="70"><circle cx="35" cy="35" r="30" fill="#1f6fbf"/></svg></div>
    <div class="badge-cell" role="img" aria-label="Manufacturer certification"><svg width="100" height="24"><rect x="0" y="4" width="100" height="16" fill="#2a3a8c"/></svg></div>
    <div class="badge-cell" role="img" aria-label="Manufacturer certification"><svg width="100" height="30"><rect x="0" y="5" width="100" height="20" fill="#2d3a4a"/></svg></div>
    <div class="badge-cell" role="img" aria-label="Manufacturer certification"><svg width="100" height="30"><rect x="0" y="5" width="100" height="20" fill="#b3262c"/></svg></div>
  </div>

  <div class="abs more"><span class="accent">AND MANY</span> MORE...</div>

  <div class="abs serving">
    <div class="serving-label">SERVING</div>
    <div class="serving-text">THE ENTIRE STATE OF ARIZONA SINCE 1984</div>
  </div>
</section>

</body>
</html>
```